Tactical Supply Company needing memorable business card design

Our tactical supply comapny is in need of a new business card design that will set us apart from the amateurs. We sell tactical gear ranging from backpacks and range bags to apparel and other gear. We are looking for a sharp design that incorporates our logo, website, and name. Our colors are white, red, and black, or any combination of the three, preferably red and black.
I have attached our logo with our name underneath but I have also edited that design with the logo incorporated next to the name (attached).

Target Market(s)

Law enforcement, military, tactical

Industry/Entity Type

Business

Contact Information for Business Card

Include www.fernhollowprovisions-demo.com

Colors
000000
ec1f27
ffffff

Requirements
Must have
• Our name, logo, and website. This is intended to be a memorable simple card, no name, address, email, or phone number info is necessary. Designs that do include this additional info will still be considered if they are absolutely spectacular.
Should not have
• A standard template design, I can create that in my own on Cardvellum. I am looking for a new, creative design that is completely unique to my company.

```html
<!DOCTYPE html>
<html lang="en">
<head>
<meta charset="utf-8">
<title>Fern Hollow Provisions – Business Card</title>
<link href="https://fonts.googleapis.com/css2?family=Open+Sans:wght@400;600;700&display=swap" rel="stylesheet">
<style>
  :root {
    --page-bg: #d9d6d1;
    --card-black: #0d0d0d;
    --card-black-soft: #1c1c1c;
    --silver-light: #f7f7f7;
    --silver-mid: #d6d6d6;
    --silver-dark: #a9a9a9;
    --brand-red: #ec1f27;
    --brand-ink: #3a3a3a;
    --text-white: #ffffff;
    --text-muted: #e6e6e6;
  }
  * { margin: 0; padding: 0; box-sizing: border-box; }
  html, body {
    width: 1200px;
    height: 1022px;
    overflow: hidden;
    background: var(--page-bg);
    font-family: "Open Sans", Arial, sans-serif;
  }
  .card {
    position: absolute;
    left: 100px;
    top: 225px;
    width: 1000px;
    height: 572px;
    border-radius: 6px;
    overflow: hidden;
    background: linear-gradient(160deg, var(--card-black-soft), var(--card-black) 60%);
    box-shadow: 0 18px 40px rgba(0,0,0,0.35);
  }
  .card-shape {
    position: absolute;
    inset: 0;
    width: 100%;
    height: 100%;
  }
  .brand {
    position: absolute;
    left: 140px;
    top: 110px;
    display: flex;
    align-items: center;
    gap: 18px;
  }
  .brand-mark {
    width: 34px;
    height: 34px;
    background: var(--brand-red);
  }
  .brand-name {
    display: flex;
    flex-direction: column;
    font-weight: 700;
    font-size: 38px;
    line-height: 1.15;
    letter-spacing: 2px;
    color: var(--brand-ink);
    text-transform: uppercase;
  }
  .contact {
    position: absolute;
    left: 80px;
    top: 395px;
    color: var(--text-white);
  }
  .person-name {
    font-weight: 700;
    font-size: 34px;
    line-height: 1.1;
  }
  .person-role {
    font-size: 18px;
    color: var(--brand-red);
    margin-bottom: 8px;
  }
  .details {
    position: absolute;
    left: 380px;
    top: 330px;
    list-style: none;
    color: var(--text-muted);
    font-size: 21px;
    line-height: 1.6;
  }
  .details li {
    display: flex;
    align-items: center;
    gap: 14px;
  }
  .detail-icon {
    width: 18px;
    height: 18px;
    flex: none;
  }
</style>
</head>
<body>
  <section class="card" aria-label="Fern Hollow Provisions business card">
    <svg class="card-shape" viewBox="0 0 1000 572" preserveAspectRatio="none" aria-hidden="true">
      <defs>
        <linearGradient id="silverPanel" x1="0" y1="0" x2="1" y2="1">
          <stop offset="0" stop-color="var(--silver-dark)"/>
          <stop offset="0.35" stop-color="var(--silver-light)"/>
          <stop offset="0.75" stop-color="var(--silver-mid)"/>
          <stop offset="1" stop-color="var(--silver-dark)"/>
        </linearGradient>
      </defs>
      <path d="M0 0 H860 C820 150 620 300 0 390 Z" fill="url(#silverPanel)"/>
      <path d="M860 0 C820 150 620 300 0 390" fill="none" stroke="var(--brand-red)" stroke-width="7"/>
    </svg>

    <div class="brand">
      <span class="brand-mark"></span>
      <span class="brand-name">
        <span class="brand-line">Fern Hollow</span>
        <span class="brand-line">Provisions</span>
      </span>
    </div>

    <div class="contact">
      <p class="person-name">Marek Tolliver</p>
      <p class="person-role">Owner</p>
    </div>

    <ul class="details">
      <li>
        <svg class="detail-icon" viewBox="0 0 18 18" aria-hidden="true"><rect width="18" height="18" rx="2" fill="var(--brand-red)"/><path d="M5 4 l2 0 1 3 -1.5 1 a7 7 0 0 0 3.5 3.5 l1-1.5 3 1 0 2 a2 2 0 0 1-2 2 A10 10 0 0 1 3 6 a2 2 0 0 1 2-2z" fill="var(--card-black)"/></svg>
        <span>00-5550-1187</span>
      </li>
      <li>
        <svg class="detail-icon" viewBox="0 0 18 18" aria-hidden="true"><rect width="18" height="18" rx="2" fill="var(--brand-red)"/><circle cx="9" cy="9" r="5" fill="none" stroke="var(--card-black)" stroke-width="1.6"/><path d="M4 9 H14 M9 4 V14" stroke="var(--card-black)" stroke-width="1.2"/></svg>
        <span>www.fernhollowprovisions-demo.com</span>
      </li>
      <li>
        <svg class="detail-icon" viewBox="0 0 18 18" aria-hidden="true"><rect width="18" height="18" rx="2" fill="var(--brand-red)"/><rect x="4" y="5" width="10" height="8" fill="none" stroke="var(--card-black)" stroke-width="1.5"/><path d="M4 5 L9 10 L14 5" fill="none" stroke="var(--card-black)" stroke-width="1.5"/></svg>
        <span>info@marektolliver-demo.com</span>
      </li>
      <li>
        <svg class="detail-icon" viewBox="0 0 18 18" aria-hidden="true"><rect width="18" height="18" rx="2" fill="var(--brand-red)"/><path d="M9 3 a4 4 0 0 1 4 4 c0 3-4 8-4 8 s-4-5-4-8 a4 4 0 0 1 4-4z" fill="var(--card-black)"/><circle cx="9" cy="7" r="1.5" fill="var(--brand-red)"/></svg>
        <span>2207 Alder Crest Road, STE 410 Ridgeport, HI 96999</span>
      </li>
    </ul>
  </section>
</body>
</html>
```